Professional Website Design to match new logo for Medical Legal Company

We have rebranded our company and We want a professional but also dynamic web site design for a group of esteemed doctors that provide expert evaluation of an injured worker in a Workers Compensation case.
​
1. Our target market is both the attorneys who select our doctors and any doctors who would wish to join our group.

2. Notes for the Landing Page:
- We prefer a simpler, sleeker more modern look for the landing page.
- We want a simplified landing page with one image, three buttons highlighted in Content document.
- We want the main image to be black and white but it can be splashed with color.
-We think the landing page might be enhanced by add a dark blue or black as a primary color. Of course please feel free to try any color combination you think might work.
- We want "The Meridale Circle" in large letters and "Stewards of a fair and prompt outcome" in small lettering. We don't want icons on the buttons.
- Do not want more than the one picture at top of landing page.
- We do not want any pictures that include faces. Please eliminate or replace. They will not be chosen.
- For the landing page, instead of a second set of photos please experiment with using medical symbols and legal symbols.
​
3. New Company Name: The Meridale Circle
New logo is uploaded bronze and grey/silver will be colors although we are still tweaking the colors for more metallic feel. Want simple not busy.

4. The overall Web page design needs to have some website design effect (e,g image rollover, scrolling effect, hover effect etc).

5. Please follow the attached word document file for the page content of the 4 web pages. Do not mix it up.

Previous company website: www.clinicjuristpanel.example (we wish to convert some of the content from this website to the new brand). Competitor website that we like: www.docboardly.example

Target Market(s)

Professional Elite. Attorneys and Doctors

Industry/Entity Type

Medical Legal

Coding

Coded - Design and coding required

Number of Pages Required

5+ page

Font styles to use
Other font styles liked:
• Helvetica or maybe font that matches logo. We are open

Colors

Designer to choose colors to be used in the design.

Requirements
Must have
• I can't locate on color scale but we want Bronze and Silver/Grey from logo. Additional colors can be added. Various shades of grey
Nice to have
• Black and white photos, simple elegant design
Should not have
• Images with faces of unknown people

```html
<!DOCTYPE html>
<html lang="en">
<head>
<meta charset="utf-8">
<title>The Meridale Circle</title>
<link href="https://fonts.googleapis.com/css2?family=Playfair+Display:wght@400;700&family=Arimo:wght@400&display=swap" rel="stylesheet">
<style>
:root{
  --bronze-dark:#9a6038;
  --bronze-light:#e0956a;
  --bronze-deep:#6e4220;
  --silver:#8c8c8c;
  --panel:#f5eee8;
  --ink:#3a3a3a;
  --text-grey:#6d6d6d;
  --footer-bg:#4a4a4a;
  --footer-line:#8a8a8a;
  --rust:#7b3524;
  --rust-light:#b87a60;
  --white:#ffffff;
}
*{margin:0;padding:0;box-sizing:border-box}
html,body{width:703px;height:1200px;overflow:hidden;background:var(--white)}
.page{position:relative;width:703px;height:1200px;overflow:hidden;font-family:"Arimo",Helvetica,Arial,sans-serif}
.abs{position:absolute}

.header{position:absolute;left:0;top:0;width:703px;height:54px;background:var(--white)}
.brand{position:absolute;left:71px;top:17px;display:flex;align-items:center;gap:6px}
.brand-mark{width:14px;height:14px;background:var(--bronze-dark)}
.brand-name{font-family:"Playfair Display",Georgia,serif;font-weight:700;font-size:13px;color:#5b5b5b}
.nav{position:absolute;top:25px;font-family:"Playfair Display",Georgia,serif;font-size:9px;color:#4b4b4b;letter-spacing:.2px}

.hero{position:absolute;left:0;top:54px;width:703px;height:366px;
  background:linear-gradient(100deg,#6b4427 0%,#9a6a45 30%,#c9b6a0 48%,#3d2c22 70%,#7d5a3c 100%)}
.hero-title{position:absolute;left:427px;top:208px;font-family:"Playfair Display",Georgia,serif;font-weight:700;font-size:27px;line-height:33px;color:var(--white)}
.hero-sub{position:absolute;left:430px;top:279px;font-family:"Playfair Display",Georgia,serif;font-weight:700;font-size:17px;line-height:21px;color:var(--white)}

.cta{position:absolute;top:476px;width:177px;height:55px;background:linear-gradient(90deg,var(--bronze-dark),var(--bronze-light));border-radius:1px;color:var(--white);text-align:center;display:flex;flex-direction:column;justify-content:center;transition:filter .2s}
.cta:hover{filter:brightness(1.1)}
.cta-title{font-family:"Playfair Display",Georgia,serif;font-weight:700;font-size:15.5px}
.cta-note{font-size:8px;margin-top:3px}

.about-symbols{position:absolute;left:72px;top:589px;width:222px;height:220px;background:var(--panel)}
.about-title{position:absolute;left:335px;top:608px;font-family:"Playfair Display",Georgia,serif;font-weight:700;font-size:30px;color:var(--ink)}
.about-text{position:absolute;left:336px;top:661px;width:288px;font-size:14.2px;line-height:17.4px;color:var(--text-grey)}

.footer{position:absolute;left:0;top:885px;width:703px;height:315px;background:var(--footer-bg)}
.f-head{position:absolute;top:979px;font-family:"Playfair Display",Georgia,serif;font-weight:700;font-size:12px;color:var(--white)}
.f-divider{position:absolute;top:982px;width:1px;height:160px;background:var(--footer-line)}
.f-link{position:absolute;left:74px;font-size:8.5px;color:var(--white)}
.f-text{position:absolute;font-size:8.5px;line-height:10.6px;color:var(--white)}
.icon-dot{position:absolute;width:27px;height:27px;border-radius:50%;background:#7b2e22;display:flex;align-items:center;justify-content:center}
.email{position:absolute;left:463px;top:1043px;width:161px;height:31px;background:var(--white);font-size:9px;color:#333;padding:10px 11px}
.download{position:absolute;left:463px;top:1081px;width:161px;height:31px;background:linear-gradient(90deg,var(--rust),var(--rust-light));color:var(--white);font-family:"Playfair Display",Georgia,serif;font-weight:700;font-size:12px;display:flex;align-items:center;justify-content:center}
.f-rule{position:absolute;left:76px;top:1142px;width:544px;height:1px;background:var(--footer-line)}
.social{position:absolute;top:1159px;width:25px;height:25px;border:1px solid var(--white);border-radius:50%}
</style>
</head>
<body>
<div class="page">

  <header class="header">
    <div class="brand"><span class="brand-mark"></span><span class="brand-name">The Meridale Circle</span></div>
    <span class="nav" style="left:316px">HOME</span>
    <span class="nav" style="left:364px">PHYSICIANS</span>
    <span class="nav" style="left:440px">STAKEHOLDER</span>
    <span class="nav" style="left:527px">MERIDALE GIVES BACK</span>
  </header>

  <section class="hero" role="img" aria-label="Black and white photo of a meeting table with a bronze colour wash"></section>
  <h1 class="hero-title">THE MERIDALE<br>CIRCLE</h1>
  <p class="hero-sub">Stewards of a fair and<br>prompt outcome</p>

  <svg class="abs" style="left:0;top:0" width="703" height="500" viewBox="0 0 703 500">
    <defs>
      <linearGradient id="bronzeL" x1="0" x2="1" y1="0" y2="0">
        <stop offset="0" stop-color="#d48a5c"/><stop offset=".2" stop-color="#7a4a20"/><stop offset=".6" stop-color="#d88d60"/><stop offset="1" stop-color="#e9a079"/>
      </linearGradient>
      <linearGradient id="bronzeR" x1="1" x2="0" y1="0" y2="0">
        <stop offset="0" stop-color="#d48a5c"/><stop offset=".2" stop-color="#7a4a20"/><stop offset=".6" stop-color="#d88d60"/><stop offset="1" stop-color="#e9a079"/>
      </linearGradient>
    </defs>
    <polygon points="0,417 350,363 703,417 703,500 0,500" fill="#fff"/>
    <polygon points="0,428 289,383 0,466" fill="url(#bronzeL)"/>
    <polygon points="404,383 703,430 703,470" fill="url(#bronzeR)"/>
  </svg>

  <a class="cta" style="left:71px"><span class="cta-title">Stake Holders</span><span class="cta-note">Attorneys, Carriers, InjuredWorkers</span></a>
  <a class="cta" style="left:260px"><span class="cta-title">QME Physicians</span></a>
  <a class="cta" style="left:448px"><span class="cta-title">Member Physicians</span></a>

  <svg class="about-symbols" viewBox="0 0 222 220" role="img" aria-label="Medical cross and scales of justice">
    <rect width="222" height="220" fill="#f5eee8"/>
    <rect x="42" y="62" width="22" height="62" fill="#9a6038"/>
    <rect x="22" y="82" width="62" height="22" fill="#9a6038"/>
    <line x1="111" y1="40" x2="111" y2="180" stroke="#c9b6a0" stroke-width="1"/>
    <g stroke="#8c8c8c" stroke-width="3" fill="none" stroke-linecap="round">
      <line x1="166" y1="58" x2="166" y2="140"/>
      <line x1="134" y1="70" x2="198" y2="70"/>
      <line x1="148" y1="140" x2="184" y2="140"/>
      <line x1="134" y1="70" x2="124" y2="104"/>
      <line x1="134" y1="70" x2="144" y2="104"/>
      <line x1="198" y1="70" x2="188" y2="104"/>
      <line x1="198" y1="70" x2="208" y2="104"/>
    </g>
    <path d="M120 104 h28 a14 9 0 0 1 -28 0z" fill="#9a6038"/>
    <path d="M184 104 h28 a14 9 0 0 1 -28 0z" fill="#9a6038"/>
    <circle cx="166" cy="56" r="4" fill="#8c8c8c"/>
  </svg>
  <h2 class="about-title">About Us</h2>
  <p class="about-text">The Meridale Circle is a leader in Qualified Medical Evaluations and SIBTF cases in the State of California. Our doctors are dedicated to facilitating settlements through rapid, objective and well researched Expert Medical Opinions</p>

  <footer class="footer"></footer>
  <svg class="abs" style="left:0;top:840px" width="703" height="120" viewBox="0 840 703 120">
    <polygon points="0,840 703,840 703,885 350,950 0,885" fill="#fff"/>
    <polygon points="0,850 283,929 0,886" fill="url(#bronzeL)"/>
    <polygon points="703,845 398,929 703,883" fill="url(#bronzeR)"/>
  </svg>

  <h3 class="f-head" style="left:74px">Links</h3>
  <h3 class="f-head" style="left:253px">Contact Us</h3>
  <h3 class="f-head" style="left:463px">Most Recent Newsletter</h3>
  <span class="f-divider" style="left:222px"></span>
  <span class="f-divider" style="left:424px"></span>

  <span class="f-link" style="top:1011px">Home</span>
  <span class="f-link" style="top:1033px">Physicians</span>
  <span class="f-link" style="top:1054px">Stakeholder</span>
  <span class="f-link" style="top:1076px">Meridale Gives Back</span>

  <span class="icon-dot" style="left:249px;top:1010px">
    <svg width="10" height="13" viewBox="0 0 10 13"><path d="M5 0C2.2 0 0 2.2 0 5c0 3.5 5 8 5 8s5-4.5 5-8C10 2.2 7.8 0 5 0z" fill="#fff"/><circle cx="5" cy="5" r="1.8" fill="#7b2e22"/></svg>
  </span>
  <p class="f-text" style="left:284px;top:1012px">HEADQUARTERS<br>2280 Linden Crest Ave.<br>4th Floor<br>Marlowe Park, CA 90412</p>
  <span class="icon-dot" style="left:247px;top:1069px">
    <svg width="12" height="12" viewBox="0 0 12 12"><path d="M2.5 0.5l2 2.3-1.1 1.5c.7 1.6 2 2.9 3.5 3.6l1.5-1.1 2.3 2-1.2 2.2C5.5 10.7 1.3 6.5 0.3 1.7z" fill="#fff"/></svg>
  </span>
  <p class="f-text" style="left:284px;top:1075px">Call toll free (800) 555-0142<br>Fax (310) 555-0187</p>

  <p class="f-text" style="left:461px;top:1009px">Lorem ipsum dolor sit amelor&nbsp; conse<br>ctt ur adipisclorem ipsumilit,</p>
  <div class="email">Email</div>
  <div class="download">Download</div>

  <span class="f-rule"></span>
  <p class="f-text" style="left:73px;top:1167px">© 2024 All Rights Reserved.Terms &amp; Conditions Privacy Policy</p>
  <span class="social" style="left:504px"></span>
  <span class="social" style="left:535px"></span>
  <span class="social" style="left:565px"></span>
  <span class="social" style="left:596px"></span>
</div>
</body>
</html>
```